Computer company startup need wordpress template

I am looking for a new design that is fresh, bold and stands out from the crowd for an IT company called Torvane Computers. We specialise in consumer and small business IT.

It will have to be mobile friendly, viewable on all devices. I need a template that i can work with and that will give our site a professional look and feel but not look like every other site out there.

To see what text will be on final site, see www.torvanecomputers-demo.com.au, i will change wording, but it is pretty close to what it's meant to be.

I have supplied logo and the main colours on car, business cards etc is black, red (and shades thereof) and white.

I am visualiing some home page with "Welcome to Torvane Computers, how may we help you today?" then 4 cool looking buttons below which says:

1. Residential computer / network issues
2. Business computer / network issues
3. Home Networking
4. New home networking

These buttons will then take you to the correct page which i will flesh out from the template. All pages need have sections for my support links etc.

Website built from template will have 5-6 pages max.

If anyone need any additional direction, please send me a message and i will answer.

Target Market(s)

Consumer and small business (1-20 employees) customers

Industry/Entity Type

It Company

Requirements
Must have
• professional look and feel

```html
<!DOCTYPE html>
<html lang="en">
<head>
<meta charset="utf-8">
<title>Torvane Computers</title>
<link href="https://fonts.googleapis.com/css2?family=Open+Sans:wght@400;600;700;800&display=swap" rel="stylesheet">
<style>
  :root {
    --red: #d3222a;
    --red-dark: #b01a21;
    --ink: #333333;
    --muted: #6b6b6b;
    --band: #eeeeee;
    --footer: #2b2b2b;
    --footer-text: #b9b9b9;
    --white: #ffffff;
  }
  * { box-sizing: border-box; margin: 0; padding: 0; }
  html, body { width: 835px; height: 1200px; overflow: hidden; }
  body { font-family: "Open Sans", Arial, sans-serif; color: var(--ink); background: var(--white); position: relative; }

  .site-header { height: 72px; position: relative; }
  .brand { position: absolute; left: 40px; top: 16px; font-size: 27px; font-weight: 800; color: var(--red); letter-spacing: -0.5px; }
  .brand::before { content: ""; display: inline-block; width: 12px; height: 12px; background: var(--red); margin-right: 8px; vertical-align: middle; }
  .callout { position: absolute; right: 40px; top: 12px; display: flex; align-items: center; gap: 10px; }
  .callout-label { font-size: 9px; line-height: 11px; text-align: right; color: var(--muted); }
  .callout-phone { font-size: 22px; font-weight: 700; color: var(--red); }
  .main-nav { position: absolute; right: 40px; top: 46px; display: flex; gap: 4px; }
  .main-nav a { font-size: 10px; font-weight: 700; color: var(--ink); text-decoration: none; padding: 5px 11px; border: 1px solid transparent; }
  .main-nav a.active { border-color: var(--red); color: var(--red); }

  .hero { position: absolute; left: 0; top: 72px; width: 835px; height: 448px; background: linear-gradient(160deg, #f4f6f9 0%, #c8d2de 35%, #6f8aa6 70%, #2d425c 100%); }
  .hero-title { position: absolute; left: 0; right: 0; top: 278px; text-align: center; color: var(--white); font-size: 23px; font-weight: 800; line-height: 30px; text-shadow: 0 1px 4px rgba(0,0,0,.5); }
  .hero-arrow { position: absolute; top: 200px; }
  .hero-dots { position: absolute; left: 0; right: 0; top: 400px; display: flex; justify-content: center; gap: 8px; }
  .hero-dots span { width: 8px; height: 8px; border-radius: 50%; background: rgba(255,255,255,.6); }
  .hero-dots span.on { background: var(--white); }

  .welcome { position: absolute; left: 70px; top: 548px; width: 700px; }
  .welcome h1 { font-size: 20px; font-weight: 700; color: var(--red); }
  .welcome h2 { font-size: 13px; font-weight: 600; margin-top: 20px; }
  .welcome-text { width: 400px; }
  .welcome-text p { font-size: 10.5px; line-height: 16px; color: var(--muted); margin-top: 12px; }
  .welcome-media { position: absolute; right: 0; top: 64px; width: 240px; height: 110px; background: linear-gradient(135deg, #e9eef4, #9fb1c5); }
  .read-more { display: inline-block; margin-top: 22px; padding: 7px 12px; border: 1px solid var(--red); color: var(--red); font-size: 9px; font-weight: 700; letter-spacing: .5px; text-decoration: none; }

  .services { position: absolute; left: 0; top: 862px; width: 835px; height: 200px; background: var(--band); }
  .service-grid { position: absolute; left: 72px; top: 32px; display: grid; grid-template-columns: 330px 330px; gap: 24px 30px; }
  .service-card { height: 52px; background: var(--white); display: flex; align-items: center; box-shadow: 0 1px 2px rgba(0,0,0,.12); }
  .service-icon { width: 52px; height: 52px; background: var(--red); display: flex; align-items: center; justify-content: center; margin-right: 16px; }
  .service-card span { font-size: 12.5px; font-weight: 600; }

  .site-footer { position: absolute; left: 0; top: 1062px; width: 835px; height: 138px; background: var(--footer); color: var(--footer-text); }
  .footer-contact { position: absolute; left: 40px; top: 22px; }
  .footer-contact h3 { font-size: 10px; font-weight: 700; color: var(--white); margin-bottom: 14px; }
  .footer-contact li { list-style: none; font-size: 9px; line-height: 18px; display: flex; align-items: center; gap: 8px; }
  .social { position: absolute; right: 40px; top: 30px; display: flex; gap: 6px; }
  .social span { width: 18px; height: 18px; border-radius: 50%; background: var(--red); }
  .footer-links { position: absolute; right: 40px; top: 66px; font-size: 9px; }
  .copyright { position: absolute; right: 40px; top: 84px; font-size: 8.5px; }
</style>
</head>
<body>
  <header class="site-header">
    <div class="brand">Torvane Computers</div>
    <div class="callout">
      <div class="callout-label">Experiencing<br>problems? call us on</div>
      <div class="callout-phone">0400 555 017</div>
    </div>
    <nav class="main-nav">
      <a class="active" href="#">HOME</a>
      <a href="#">SERVICES</a>
      <a href="#">ABOUT US</a>
      <a href="#">CONTACT US</a>
      <a href="#">FAQS</a>
    </nav>
  </header>

  <section class="hero" role="img" aria-label="Photo of a row of computer workstations in an office">
    <svg class="hero-arrow" style="left:24px" width="20" height="34" viewBox="0 0 20 34"><path d="M17 3 4 17l13 14" fill="none" stroke="#fff" stroke-width="4"/></svg>
    <svg class="hero-arrow" style="right:24px" width="20" height="34" viewBox="0 0 20 34"><path d="M3 3l13 14L3 31" fill="none" stroke="#fff" stroke-width="4"/></svg>
    <div class="hero-title">THE CHOICE FOR PROACTIVE,<br>OUTSOURCED I.T. SUPPORT</div>
    <div class="hero-dots"><span class="on"></span><span></span><span></span><span></span><span></span></div>
  </section>

  <section class="welcome">
    <h1>Welcome to Torvane Computers</h1>
    <h2>How may we help you today?</h2>
    <div class="welcome-text">
      <p>Torvane Computers deliver expert onsite computer services to small businesses and home owners in Southern Tasmania. We specialise in IT security, custom built computers and general computer repair.</p>
      <p>Our expert staff will also help you with training and pre purchase advice to what suits your business or family best, and what will also future proof you in the areas where your system will be utilised the most. The best thing is that WE'LL COME TO YOU.</p>
      <a class="read-more" href="#">READ MORE</a>
    </div>
    <div class="welcome-media" role="img" aria-label="Photo of a computer workstation"></div>
  </section>

  <section class="services">
    <div class="service-grid">
      <a class="service-card">
        <div class="service-icon"><svg width="24" height="22" viewBox="0 0 24 22"><path d="M2 11 12 2l10 9h-3v10h-5v-6h-4v6H5V11z" fill="#fff"/></svg></div>
        <span>Residential Computer / Network Issues</span>
      </a>
      <a class="service-card">
        <div class="service-icon"><svg width="22" height="22" viewBox="0 0 22 22"><path d="M3 21V3h10v6h6v12z" fill="#fff"/><path d="M6 6h2v2H6zm0 4h2v2H6zm0 4h2v2H6zm10-1h2v2h-2zm0 4h2v2h-2z" fill="#d3222a"/></svg></div>
        <span>Business Computer / Network Issues</span>
      </a>
      <a class="service-card">
        <div class="service-icon"><svg width="24" height="22" viewBox="0 0 24 22"><path d="M2 11 12 2l10 9h-3v10h-5v-6h-4v6H5V11z" fill="#fff"/></svg></div>
        <span>Home Networking</span>
      </a>
      <a class="service-card">
        <div class="service-icon"><svg width="22" height="22" viewBox="0 0 22 22"><path d="M3 21V3h10v6h6v12z" fill="#fff"/><path d="M6 6h2v2H6zm0 4h2v2H6zm0 4h2v2H6zm10-1h2v2h-2zm0 4h2v2h-2z" fill="#d3222a"/></svg></div>
        <span>New Home Networking</span>
      </a>
    </div>
  </section>

  <footer class="site-footer">
    <div class="footer-contact">
      <h3>CONTACT US</h3>
      <ul>
        <li><svg width="8" height="11" viewBox="0 0 8 11"><path d="M4 0a4 4 0 0 0-4 4c0 3 4 7 4 7s4-4 4-7a4 4 0 0 0-4-4z" fill="#b9b9b9"/></svg>14 Example Street, Sandy Bay TAS 7005</li>
        <li><svg width="8" height="11" viewBox="0 0 8 11"><rect x="1" y="0" width="6" height="11" rx="1" fill="#b9b9b9"/></svg>0400 555 017</li>
        <li><svg width="10" height="8" viewBox="0 0 10 8"><rect width="10" height="8" fill="#b9b9b9"/><path d="M0 0l5 4 5-4" fill="none" stroke="#2b2b2b"/></svg>info@torvanecomputers-demo.com.au</li>
      </ul>
    </div>
    <div class="social"><span></span><span></span><span></span><span></span></div>
    <div class="footer-links">Home &nbsp;|&nbsp; News &nbsp;|&nbsp; Services &nbsp;|&nbsp; About us &nbsp;|&nbsp; Contact us &nbsp;|&nbsp; Fax</div>
    <div class="copyright">Copyright © 2015 All Rights Reserved</div>
  </footer>
</body>
</html>
```